A5 Magazine Cover Design

I need a front cover designing for a new community magazine called HOMLEY. HOMLEY will be listing local buisnesses and local interest articles for the residents in my area. I need the look to be clean but inviting.

I will consider any colour combination as long as its not too bright.

```html
<!DOCTYPE html>
<html lang="en">
<head>
<meta charset="utf-8">
<title>HOMLEY – Community Magazine Cover</title>
<link rel="stylesheet" href="https://fonts.googleapis.com/css2?family=Open+Sans:wght@700;800&display=swap">
<style>
  :root {
    --cover-orange: #d8670a;
    --band-mist: #edf2f0;
  }
  html, body {
    margin: 0;
    padding: 0;
    width: 846px;
    height: 1200px;
    overflow: hidden;
    background: var(--cover-orange);
  }
  .cover {
    display: block;
    width: 846px;
    height: 1200px;
  }
  .cover__ground { fill: var(--cover-orange); }
  .cover__rule,
  .cover__band { fill: var(--band-mist); }
  .cover__masthead {
    font-family: "Open Sans", sans-serif;
    font-weight: 800;
    fill: var(--cover-orange);
  }
  .cover__tagline {
    font-family: "Open Sans", sans-serif;
    font-weight: 700;
    fill: var(--band-mist);
  }
</style>
</head>
<body>
<svg class="cover" viewBox="0 0 1000 1419" xmlns="http://www.w3.org/2000/svg" aria-label="HOMLEY magazine cover">
  <rect class="cover__ground" x="0" y="0" width="1000" height="1419"/>

  <rect class="cover__rule cover__rule--inner" x="920" y="-10" width="20" height="1232" rx="4"/>
  <rect class="cover__rule cover__rule--outer" x="952" y="300" width="24" height="1130"/>

  <polygon class="cover__band" points="0,390 1000,238 1000,492 0,647"/>

  <text class="cover__masthead" x="58" y="590" font-size="258" textLength="885" lengthAdjust="spacingAndGlyphs" transform="rotate(-8.6 58 590)">HOMLEY</text>

  <text class="cover__tagline" x="138" y="674" font-size="41" textLength="775" lengthAdjust="spacingAndGlyphs" transform="rotate(-8.6 138 674)">searches , reviews and recommends locally</text>
</svg>
</body>
</html>
```